Brightwell Consulting Business Card Design

Business Card Design for Brightwell Consulting. Brightwell Consulting is a boutique consultancy based in Atlanta, GA., that specializes in marketing strategy, organization planning, and leadership development. We provide solutions for small businesses and startups as well as Summit 400 companies.

http://brightwellconsulting.example/

Target Market(s)

We provide solutions for small businesses and startups as well as Summit 400 companies.

Industry/Entity Type

Consulting

Contact Information for Business Card

Two sided business card with priority on contact information, logo, tag line (Inspiration to Dream More, Do More, Become More)

Colors

Designer to choose colors to be used in the design.

Requirements
Must have
• contact information, logo, tag line (Inspiration to Dream More, Do More, Become More)
• Simple no over communication.
Nice to have
• I would like to see different placements of logo and creative use of both sides of the card
Should not have
• Do not put too much information on the card.

```html
<!DOCTYPE html>
<html lang="en">
<head>
<meta charset="utf-8">
<title>Brightwell Consulting Business Card</title>
<link rel="stylesheet" href="https://fonts.googleapis.com/css2?family=Montserrat:wght@400;500&display=swap">
<style>
  :root {
    --navy: #1e3554;
    --orange: #f7931e;
    --white: #ffffff;
    --green: #3a9a3a;
    --backdrop: #e9e6e1;
  }
  * { box-sizing: border-box; margin: 0; padding: 0; }
  html, body { width: 1200px; height: 1000px; overflow: hidden; }
  body {
    position: relative;
    background: var(--backdrop);
    font-family: "Montserrat", sans-serif;
  }
  .card {
    position: absolute;
    width: 600px;
    height: 360px;
    box-shadow: 0 6px 18px rgba(0,0,0,0.25);
  }
  /* Front */
  .card-front { left: 195px; top: 103px; background: var(--white); }
  .front-top-rule {
    position: absolute; left: 0; right: 0; top: 7px; height: 8px;
    background: var(--navy);
  }
  .name-frame {
    position: absolute; left: 144px; top: 106px; width: 312px; height: 74px;
    border: 3px solid var(--navy);
  }
  .name-line {
    position: absolute; left: 0; right: 0; top: 18px;
    text-align: center; font-size: 30px; font-weight: 500; letter-spacing: 0.5px;
    color: var(--navy); line-height: 1; white-space: nowrap;
  }
  .name-line .surname { color: var(--orange); }
  .frame-caption {
    position: absolute; left: 50%; bottom: -10px; transform: translateX(-50%);
    background: var(--white); padding: 0 12px;
    font-size: 15px; letter-spacing: 0.5px; color: var(--navy); line-height: 1;
    white-space: nowrap;
  }
  .contact-band {
    position: absolute; left: 0; right: 0; top: 285px; height: 61px;
    background: var(--navy);
    display: flex; align-items: center; justify-content: space-between;
    padding: 0 16px;
  }
  .contact-item {
    display: flex; align-items: center; gap: 9px;
    color: var(--white); font-size: 12px; white-space: nowrap; flex-shrink: 0;
  }
  .contact-item svg { width: 11px; height: 11px; fill: var(--green); flex-shrink: 0; }
  /* Back */
  .card-back { left: 405px; top: 536px; background: var(--navy); }
  .brand-name {
    position: absolute; left: 0; right: 0; top: 150px;
    text-align: center; color: var(--white);
    font-size: 34px; font-weight: 500; letter-spacing: 1px; white-space: nowrap;
  }
  .tagline-band {
    position: absolute; left: 0; right: 0; top: 287px; height: 28px;
    background: var(--white);
    display: flex; align-items: center; justify-content: center;
    color: var(--orange); font-size: 14px; white-space: nowrap;
  }
  .address {
    position: absolute; left: 0; right: 0; top: 330px;
    display: flex; align-items: center; justify-content: center; gap: 14px;
    color: var(--white); font-size: 13.5px; white-space: nowrap;
  }
  .address svg { width: 11px; height: 14px; fill: var(--white); }
</style>
</head>
<body>
  <section class="card card-front">
    <div class="front-top-rule"></div>
    <div class="name-frame">
      <div class="name-line">NAME <span class="surname">SURNAME</span></div>
      <div class="frame-caption">CONSULTING</div>
    </div>
    <div class="contact-band">
      <div class="contact-item">
        <svg viewBox="0 0 24 24"><path d="M6.6 10.8a15.1 15.1 0 0 0 6.6 6.6l2.2-2.2a1 1 0 0 1 1-.25 11.4 11.4 0 0 0 3.6.57 1 1 0 0 1 1 1V20a1 1 0 0 1-1 1A17 17 0 0 1 3 4a1 1 0 0 1 1-1h3.5a1 1 0 0 1 1 1c0 1.25.2 2.45.57 3.57a1 1 0 0 1-.25 1z"/></svg>
        <span>555-010-2468</span>
      </div>
      <div class="contact-item">
        <svg viewBox="0 0 24 24"><path d="M2 5h20v2l-10 6L2 7z M2 9.3l10 6 10-6V19H2z"/></svg>
        <span>hi@brightwellconsulting.example</span>
      </div>
      <div class="contact-item">
        <svg viewBox="0 0 24 24"><circle cx="12" cy="12" r="10"/></svg>
        <span>brightwellconsulting.example</span>
      </div>
    </div>
  </section>

  <section class="card card-back">
    <div class="brand-name">Brightwell Consulting</div>
    <div class="tagline-band">Inspiration to Dream More, Do More, Become More</div>
    <div class="address">
      <svg viewBox="0 0 12 16"><path d="M6 0a6 6 0 0 0-6 6c0 4.5 6 10 6 10s6-5.5 6-10a6 6 0 0 0-6-6zm0 8.2A2.2 2.2 0 1 1 6 3.8a2.2 2.2 0 0 1 0 4.4z"/></svg>
      <span>2150 Linden Ave 400, Atlanta, GA</span>
    </div>
  </section>
</body>
</html>
```